Signage. Will be for store front. Building is on a corner lot. Lots of traffic.

Opening a new location for our landscape business with a garden store (boutique theme) which will have big pottery pots, house plants, ferns and orchids for sale.

And on the side lot of the store we will have bigger bulk items(contractors theme) landscape plants, sod, mulch, soil, rock for sale.

Sign is about 8’x6’

Target Market(s)

Home owners
Landscapers
Builders

Industry/Entity Type

Landscaping

Font styles to use
Sans Serif

Colors
9bcb3c

Requirements
Must have
• “ Installation and Delivery” is a big deal to let people know we do that
Nice to have
• Added a first rendition idea but don’t love it
Added a file with some words to play with
Need help with the words
Should not have
• ?

```html
<!DOCTYPE html>
<html lang="en">
<head>
<meta charset="utf-8">
<title>Verdant Ridge Outdoors – Storefront Sign</title>
<link rel="stylesheet" href="https://fonts.googleapis.com/css2?family=Montserrat:ital,wght@0,800;1,800;1,900&display=swap">
<style>
  :root {
    --lime: #9bcb3c;
    --lime-deep: #7fb22a;
    --forest: #0b3d1a;
    --charcoal: #333331;
    --white: #ffffff;
    --sky: #6f9fd8;
    --soil: #8a7561;
    --grass: #4f9a2a;
  }
  * { margin: 0; padding: 0; box-sizing: border-box; }
  html, body { width: 1200px; height: 900px; overflow: hidden; background: var(--white); }
  .sign {
    position: relative;
    width: 1200px;
    height: 900px;
    background: var(--white);
    font-family: "Montserrat", Arial, sans-serif;
    overflow: hidden;
  }
  .brand {
    position: absolute;
    left: 57px;
    top: 58px;
    display: flex;
    align-items: center;
    gap: 22px;
  }
  .brand-name {
    font-weight: 800;
    font-size: 52px;
    line-height: 1.08;
    color: var(--forest);
    letter-spacing: 1px;
    text-transform: uppercase;
  }
  .brand-dot {
    width: 70px;
    height: 70px;
    border-radius: 50%;
    background: var(--lime);
  }
  .headline-band { position: absolute; left: 0; top: 230px; }
  .headline {
    position: absolute;
    left: 54px;
    top: 246px;
    font-weight: 900;
    font-style: italic;
    font-size: 79px;
    line-height: 0.88;
    letter-spacing: -1px;
    color: var(--charcoal);
    text-transform: uppercase;
  }
  .offer-list {
    position: absolute;
    top: 432px;
    list-style: none;
  }
  .offer-list.left { left: 57px; }
  .offer-list.right { left: 450px; }
  .offer-list li {
    position: relative;
    padding-left: 26px;
    font-weight: 800;
    font-style: italic;
    font-size: 28px;
    line-height: 46.7px;
    color: var(--forest);
    text-transform: uppercase;
    white-space: nowrap;
  }
  .offer-list li::before {
    content: "";
    position: absolute;
    left: 0;
    top: 17px;
    border-left: 10px solid var(--forest);
    border-top: 6px solid transparent;
    border-bottom: 6px solid transparent;
  }
  .offer-list li.continued { padding-left: 26px; }
  .offer-list li.continued::before { display: none; }
  .hero-photo { position: absolute; left: 728px; top: 40px; }
  .ground { position: absolute; left: 0; top: 712px; }
  .work-photo { position: absolute; top: 669px; }
</style>
</head>
<body>
<main class="sign">

  <div class="brand">
    <div class="brand-name">Verdant Ridge<br>Outdoors</div>
    <div class="brand-dot"></div>
  </div>

  <svg class="headline-band" width="780" height="168" viewBox="0 0 780 168" aria-hidden="true">
    <path d="M0 0 H698 C640 40 500 100 484 168 H0 Z" fill="var(--lime)"/>
  </svg>
  <h1 class="headline">Installation<br>and Delivery</h1>

  <ul class="offer-list left">
    <li>Garden Center</li>
    <li>Landscape Supply</li>
    <li>Garden Shop</li>
    <li>Garden Supply</li>
    <li>Lawn &amp; Garden</li>
  </ul>
  <ul class="offer-list right">
    <li>Nursery &amp;</li>
    <li class="continued">Garden</li>
    <li>Nursery</li>
    <li>Sod</li>
    <li>Landscaping</li>
  </ul>

  <svg class="hero-photo" width="448" height="582" viewBox="0 0 448 582" role="img" aria-label="Photo of the landscaping crew in bright green shirts holding tools on a job site">
    <defs>
      <linearGradient id="heroTone" x1="0" y1="0" x2="0" y2="1">
        <stop offset="0" stop-color="var(--sky)"/>
        <stop offset="0.4" stop-color="#9fc86a"/>
        <stop offset="1" stop-color="var(--soil)"/>
      </linearGradient>
    </defs>
    <path d="M40 0 H408 A40 40 0 0 1 448 40 V358 A224 224 0 0 1 0 358 V40 A40 40 0 0 1 40 0 Z" fill="url(#heroTone)"/>
  </svg>

  <svg class="ground" width="1200" height="188" viewBox="0 0 1200 188" role="img" aria-label="Grass border along the bottom of the sign">
    <defs>
      <linearGradient id="grassTone" x1="0" y1="0" x2="0" y2="1">
        <stop offset="0" stop-color="var(--grass)"/>
        <stop offset="1" stop-color="var(--lime)"/>
      </linearGradient>
    </defs>
    <rect x="0" y="0" width="1200" height="50" fill="url(#grassTone)"/>
    <rect x="0" y="50" width="1200" height="138" fill="var(--lime)"/>
  </svg>

  <svg class="work-photo" style="left:123px" width="192" height="192" viewBox="0 0 192 192" role="img" aria-label="Photo of crew digging a planting bed with equipment">
    <circle cx="96" cy="96" r="96" fill="var(--white)"/>
    <circle cx="96" cy="96" r="84" fill="#5d6b3d"/>
  </svg>
  <svg class="work-photo" style="left:377px" width="192" height="192" viewBox="0 0 192 192" role="img" aria-label="Photo of a worker placing plants beside a waterfront lawn">
    <circle cx="96" cy="96" r="96" fill="var(--white)"/>
    <circle cx="96" cy="96" r="84" fill="#7fa3a8"/>
  </svg>
  <svg class="work-photo" style="left:632px" width="192" height="192" viewBox="0 0 192 192" role="img" aria-label="Photo of crew carrying sod rolls across a yard">
    <circle cx="96" cy="96" r="96" fill="var(--white)"/>
    <circle cx="96" cy="96" r="84" fill="#86a86a"/>
  </svg>
  <svg class="work-photo" style="left:887px" width="192" height="192" viewBox="0 0 192 192" role="img" aria-label="Photo of workers laying fresh sod">
    <circle cx="96" cy="96" r="96" fill="var(--white)"/>
    <circle cx="96" cy="96" r="84" fill="#7d9a55"/>
  </svg>

</main>
</body>
</html>
```